Marolina Swimming & Athletics Center

We need Business Card for a Athletics center
The logo frome the Uploaded Files ( b card fimal)
Οn one side of card we need the logo of company the Contact and the website:
1. Address:(Limassol, Cyprus 12-14 Dravelonos str,Ano Feralia,P.C. 5280)

2.Phone number: (+357) 25-804273

3. Mail: info@marolinasport.example

3. Website: www.marolinasport.example

Οn the other side of the card we need to write the sport of the company:

1. Artistic Gymnastics
2. Swimming
3. Gym - Fitness
4. Programs
5. Dancing
5.Tennis

From the Uploaded Files you can get the logo.In a logo is behind the black color which can be removed from logo.

Υou can use that color you want.
.

Industry/Entity Type

Business

Font styles to use
Decorative

Colors
0555a3
ffcf3e
3176b5
0692cd
add136
f04a50
000000
cfcfcf
9d9d9d

Requirements
Should not have
• photos with faces
• photo fro the Website:www.marolinasport.example

```html
<!DOCTYPE html>
<html lang="en">
<head>
<meta charset="utf-8">
<title>Marolina Swimming &amp; Athletics Center – Business Card</title>
<link rel="stylesheet" href="https://fonts.googleapis.com/css2?family=Montserrat:wght@400;600;800&family=Didact+Gothic&display=swap">
<style>
  :root {
    --yellow: #f5d33f;
    --ink: #1d1a21;
    --gold: #f2b21c;
    --orange: #f29a2e;
    --photo-dark: #2b2b2b;
    --photo-light: #8a8a8a;
    --backdrop: #e6e2dc;
    --text: #1f1f1f;
  }
  * { box-sizing: border-box; margin: 0; padding: 0; }
  html, body { width: 1200px; height: 751px; overflow: hidden; }
  body {
    background: var(--backdrop);
    font-family: "Didact Gothic", "Montserrat", sans-serif;
    color: var(--text);
    position: relative;
  }
  .card {
    position: absolute;
    top: 216px;
    width: 540px;
    height: 318px;
    overflow: hidden;
    box-shadow: 0 6px 18px rgba(0,0,0,.18);
  }
  .card--front { left: 40px; background: var(--yellow); }
  .card--back  { left: 620px; background: var(--yellow); }

  /* front */
  .front__band {
    position: absolute; left: 0; right: 0; top: 92px; height: 74px;
    background: var(--ink);
    display: flex; align-items: center; justify-content: center; gap: 16px;
  }
  .brand {
    font-family: "Montserrat", sans-serif;
    font-weight: 800;
    color: var(--gold);
    letter-spacing: 3px;
  }
  .front__band .brand { font-size: 34px; }
  .brand-mark {
    border-radius: 50%;
    background: var(--gold);
    flex: none;
  }
  .front__band .brand-mark { width: 40px; height: 40px; }
  .front__services {
    position: absolute; left: 0; right: 0; top: 186px;
    text-align: center; font-size: 17px; line-height: 1.45;
  }

  /* back */
  .back__photo {
    position: absolute; left: 0; top: 0; width: 300px; height: 100%;
    background: radial-gradient(ellipse at 55% 55%, var(--photo-light) 0%, var(--photo-dark) 75%);
  }
  .back__logo-band {
    position: absolute; left: 0; top: 70px; width: 300px; height: 62px;
    background: var(--ink);
    display: flex; align-items: center; justify-content: center; gap: 12px;
  }
  .back__logo-band .brand { font-size: 26px; }
  .back__logo-band .brand-mark { width: 30px; height: 30px; }

  .contact {
    position: absolute; left: 300px; top: 0; width: 240px; height: 100%;
    display: flex; flex-direction: column;
  }
  .contact__row {
    position: relative;
    display: flex; align-items: center;
    padding-left: 20px;
    border-bottom: 7px solid var(--ink);
    font-size: 14px;
    flex: none;
  }
  .contact__row:last-child { border-bottom: 0; flex: 1; }
  .contact__title { height: 82px; flex-direction: column; align-items: flex-start; justify-content: center; }
  .contact__title strong { font-family: "Montserrat", sans-serif; font-weight: 800; font-size: 15px; }
  .contact__title span { font-size: 14px; letter-spacing: .5px; }
  .contact__line { height: 50px; }
  .contact__address { flex-direction: column; align-items: flex-start; justify-content: center; line-height: 1.35; }
  .contact__icon {
    position: absolute; left: -26px; top: 50%; transform: translateY(-50%);
    width: 36px; height: 28px; border-radius: 6px;
    background: var(--orange);
    display: flex; align-items: center; justify-content: center;
  }
  .contact__icon svg { width: 18px; height: 18px; }
</style>
</head>
<body>

<section class="card card--front" aria-label="Business card front">
  <div class="front__band">
    <span class="brand">MAROLINA</span>
    <span class="brand-mark"></span>
  </div>
  <p class="front__services">
    • Artistic Gymnastics • Swimming • Gym - Fitness<br>
    • Programs • Dancing • Tennis
  </p>
</section>

<section class="card card--back" aria-label="Business card back">
  <div class="back__photo" role="img" aria-label="Black and white photograph of athletes in dynamic dance poses"></div>
  <div class="back__logo-band">
    <span class="brand">MAROLINA</span>
    <span class="brand-mark"></span>
  </div>

  <div class="contact">
    <div class="contact__row contact__title">
      <strong>MAROLINA SWIMMING</strong>
      <span>&amp; ATHLETICS CENTER</span>
    </div>
    <div class="contact__row contact__line">
      <span class="contact__icon">
        <svg viewBox="0 0 24 24"><path fill="#1d1a21" d="M6.6 10.8a15.1 15.1 0 0 0 6.6 6.6l2.2-2.2c.3-.3.7-.4 1-.2 1.1.4 2.3.6 3.6.6.6 0 1 .4 1 1V20c0 .6-.4 1-1 1A17 17 0 0 1 3 4c0-.6.4-1 1-1h3.5c.6 0 1 .4 1 1 0 1.3.2 2.5.6 3.6.1.3 0 .7-.2 1z"/></svg>
      </span>
      (+357) 25-804273
    </div>
    <div class="contact__row contact__line">
      <span class="contact__icon">
        <svg viewBox="0 0 24 24" fill="none" stroke="#1d1a21" stroke-width="2"><rect x="3" y="5" width="18" height="14"/><path d="M3 5l9 8 9-8"/></svg>
      </span>
      info@marolinasport.example
    </div>
    <div class="contact__row contact__line">
      <span class="contact__icon">
        <svg viewBox="0 0 24 24" fill="none" stroke="#1d1a21" stroke-width="2.2" stroke-linecap="round"><path d="M10 14a4 4 0 0 0 5.7 0l3-3a4 4 0 0 0-5.7-5.7l-1 1"/><path d="M14 10a4 4 0 0 0-5.7 0l-3 3a4 4 0 0 0 5.7 5.7l1-1"/></svg>
      </span>
      www.marolinasport.example
    </div>
    <div class="contact__row contact__address">
      <span>Limassol, Cyprus 12-14</span>
      <span>Dravelonos str,</span>
      <span>Ano Feralia,P.C. 5280</span>
    </div>
  </div>
</section>

</body>
</html>
```